Fund Harbor

We need desigin for our main page(concept will be used for other pages also).
We already have a logo, and moqup of our main page(see attch).
You could change layers and positions on moqup, but please use logo, and its colors in design creating. (We have logo in different colors, i attached 2 samples, so you could use also another colors if you wish).

Our bussinees will be something similar to LaunchPeak or Backwise.co, but with some special features. So main idea: start-ups, donations, investemnets

Designs were prefer:
http://backwise.co/
http://www.launchpeak.com/

Target Market(s)

Clients are middle aged persons, who interested in new start-ups, investments and so on.

Requirements
Must have
• Design must be neat

```html
<!DOCTYPE html>
<html lang="en">
<head>
<meta charset="utf-8">
<title>Fund Harbor</title>
<link rel="stylesheet" href="https://fonts.googleapis.com/css2?family=Arimo:wght@400;700&family=Questrial&display=swap">
<style>
:root{
  --red:#d63b3b;
  --red-dark:#a80000;
  --red-nav:#d2352f;
  --black:#000;
  --card-top:#3a3a3a;
  --card-bottom:#161616;
  --footer:#2a2a2a;
  --grey-text:#b5b5b5;
  --white:#fff;
}
*{margin:0;padding:0;box-sizing:border-box}
html,body{width:1200px;height:1200px;overflow:hidden}
body{position:relative;background:var(--white);font-family:"Arimo",Arial,sans-serif;color:var(--white)}
.abs{position:absolute}

.topbar{left:0;top:0;width:1200px;height:31px;background:var(--black)}
.lang{left:866px;top:2px;width:79px;height:25px;background:var(--white);color:#000;font-size:14px;padding:5px 3px;border:1px solid #888}
.lang .arrow{position:absolute;right:1px;top:1px;width:20px;height:21px;background:#ddd;border-left:1px solid #888;font-size:10px;text-align:center;line-height:21px}
.search{left:954px;top:2px;width:139px;height:25px;background:var(--white);color:#000;font-size:14px;padding:5px 7px}
.search svg{position:absolute;right:6px;top:2px}

.header{left:0;top:31px;width:1200px;height:567px;background:radial-gradient(ellipse at 50% 35%,#f4f4f4 0%,#cfcfcf 55%,#9d9d9d 100%)}
.brand{left:120px;top:88px;display:flex;align-items:center;gap:8px;font-family:"Questrial",sans-serif;font-size:28px;color:#333}
.brand .mark{width:18px;height:18px;background:var(--red);border-radius:50%}
.nav{top:97px;font-family:"Questrial",sans-serif;font-size:15px;color:var(--red-nav)}
.account{top:97px;font-family:"Questrial",sans-serif;font-size:15px;color:var(--white)}

.hero{left:113px;top:137px;width:980px;height:414px;border-radius:6px;overflow:hidden;box-shadow:0 3px 6px rgba(0,0,0,.35)}
.hero-photo{position:absolute;left:312px;top:0;width:668px;height:414px;background:linear-gradient(160deg,#c9dcef 0%,#eef3f8 40%,#9aa4ad 70%,#3d4046 100%)}
.hero-stats{position:absolute;left:0;top:0;width:312px;height:414px;background:var(--red)}
.stat{position:absolute;left:15px;display:flex;align-items:center;gap:10px;font-size:17px}
.stat svg{flex:none}

.card{top:574px;height:295px;border-radius:4px;background:linear-gradient(180deg,var(--card-top),var(--card-bottom));text-align:center}
.card h2{margin-top:11px;font-family:"Questrial",sans-serif;font-weight:400;font-size:17px}
.card .sub{color:var(--grey-text);font-size:14px;line-height:17px;margin-top:3px}
.card ul{list-style:none;text-align:left;margin:14px 0 0 36px;font-size:13px;line-height:15px}
.card li{position:relative;padding-left:14px;margin-bottom:15px}
.card li::before{content:"";position:absolute;left:0;top:4px;width:6px;height:6px;border-radius:50%;background:#e01010}
.more{position:absolute;left:48px;top:257px;width:100px;height:31px;border-radius:6px;background:linear-gradient(180deg,#e61c1c,#a50000);font-size:13px;line-height:31px;text-align:center}

.band{left:0;top:955px;width:1200px;height:98px;background:var(--red-dark);border-top:3px solid #c51a1a}
.band-text{left:386px;top:991px;font-size:25px}
.yes{left:961px;top:984px;width:104px;height:43px;border-radius:6px;background:var(--black);font-size:24px;text-align:center;line-height:48px}

.footer{left:0;top:1053px;width:1200px;height:147px;background:radial-gradient(ellipse at 70% 40%,#444 0%,var(--footer) 60%,#1f1f1f 100%)}
.map{left:752px;top:1062px;width:335px;height:132px;background:radial-gradient(ellipse,rgba(190,190,190,.35),rgba(120,120,120,0) 70%)}
.flink{font-size:10px;color:var(--white)}

.video{left:114px;top:885px;width:227px;height:186px;background:var(--black);box-shadow:0 2px 5px rgba(0,0,0,.5)}
.video .controls{position:absolute;left:0;bottom:0;width:227px;height:16px;background:linear-gradient(#ddd,#9a9a9a)}
</style>
</head>
<body>
<div class="abs topbar"></div>
<div class="abs lang">English<span class="arrow">▼</span></div>
<div class="abs search">Search ...
  <svg width="22" height="22" viewBox="0 0 22 22"><circle cx="9" cy="9" r="6" fill="none" stroke="#555" stroke-width="2"/><line x1="13" y1="13" x2="19" y2="19" stroke="#555" stroke-width="3"/></svg>
</div>

<div class="abs header"></div>
<div class="abs brand"><span class="mark"></span>Fund Harbor</div>
<nav>
  <span class="abs nav" style="left:350px">Home</span>
  <span class="abs nav" style="left:426px">How it works</span>
  <span class="abs nav" style="left:545px">Project Review</span>
  <span class="abs nav" style="left:673px">Visit Office</span>
  <span class="abs account" style="left:958px">LOGIN</span>
  <span class="abs account" style="left:1024px">REGISTER</span>
</nav>

<section class="abs hero">
  <div class="hero-photo" role="img" aria-label="Cheering businessman at a laptop in a bright office, coins and a seedling in the foreground"></div>
  <div class="hero-stats">
    <div class="stat" style="top:48px"><svg width="21" height="21"><circle cx="10.5" cy="10.5" r="10.5" fill="#3a0a0a"/><path d="M5 11l4 4 7-9" stroke="#fff" stroke-width="2.5" fill="none"/></svg>$ 50 000 000 of investments</div>
    <div class="stat" style="top:98px"><svg width="21" height="21"><circle cx="10.5" cy="10.5" r="10.5" fill="#3a0a0a"/><path d="M5 11l4 4 7-9" stroke="#fff" stroke-width="2.5" fill="none"/></svg>1600 start - ups</div>
    <div class="stat" style="top:148px"><svg width="21" height="21"><circle cx="10.5" cy="10.5" r="10.5" fill="#3a0a0a"/><path d="M5 11l4 4 7-9" stroke="#fff" stroke-width="2.5" fill="none"/></svg>700 organizations</div>
    <div class="stat" style="top:198px"><svg width="21" height="21"><circle cx="10.5" cy="10.5" r="10.5" fill="#3a0a0a"/><path d="M5 11l4 4 7-9" stroke="#fff" stroke-width="2.5" fill="none"/></svg>10 000 investors</div>
    <div class="stat" style="top:248px"><svg width="21" height="21"><circle cx="10.5" cy="10.5" r="10.5" fill="#3a0a0a"/><path d="M5 11l4 4 7-9" stroke="#fff" stroke-width="2.5" fill="none"/></svg>5000 employess</div>
    <div class="stat" style="top:298px"><svg width="21" height="21"><circle cx="10.5" cy="10.5" r="10.5" fill="#3a0a0a"/><path d="M5 11l4 4 7-9" stroke="#fff" stroke-width="2.5" fill="none"/></svg>2000 partners</div>
    <div class="stat" style="top:348px"><svg width="21" height="21"><circle cx="10.5" cy="10.5" r="10.5" fill="#3a0a0a"/><path d="M5 11l4 4 7-9" stroke="#fff" stroke-width="2.5" fill="none"/></svg>$ 10 000 000 of profit</div>
  </div>
</section>

<article class="abs card" style="left:198px;width:197px">
  <h2>RECOMMENDED</h2><p class="sub">Claritas est etiam<br>processus dynamicus</p>
  <ul><li>Duis autem vel eum iriure dolor</li><li>An hendrerit in vulputate velit esse molestie consequat</li><li>vel illum dolore eu feugiat nulla facilisis at vero eros et accumsan et iusto</li></ul>
  <span class="more">More</span>
</article>
<article class="abs card" style="left:399px;width:198px">
  <h2>POPULAR</h2><p class="sub">Claritas est etiam<br>processus dynamicus</p>
  <ul><li>Duis autem vel eum iriure dolor</li><li>An hendrerit in vulputate velit esse molestie consequat</li><li>vel illum dolore eu feugiat nulla facilisis at vero eros et accumsan et iusto</li></ul>
  <span class="more" style="left:53px">More</span>
</article>
<article class="abs card" style="left:602px;width:197px">
  <h2>MOST VIEWED</h2><p class="sub">Claritas est etiam<br>processus dynamicus</p>
  <ul><li>Duis autem vel eum iriure dolor</li><li>An hendrerit in vulputate velit esse molestie consequat</li><li>vel illum dolore eu feugiat nulla facilisis at vero eros et accumsan et iusto</li></ul>
  <span class="more" style="left:52px">More</span>
</article>
<article class="abs card" style="left:808px;width:198px">
  <h2>NEW</h2><p class="sub">Claritas est etiam<br>processus dynamicus</p>
  <ul style="margin-left:38px"><li>Duis autem vel eum iriure dolor</li><li>An hendrerit in vulputate velit esse molestie consequat</li><li>vel illum dolore eu feugiat nulla facilisis at vero eros et accumsan et iusto</li></ul>
  <span class="more" style="left:49px">More</span>
</article>

<div class="abs band"></div>
<p class="abs band-text">VIEW&nbsp; ALL PROJECTS? More than 1000 projects</p>
<span class="abs yes">YES</span>

<footer class="abs footer"></footer>
<div class="abs map" role="img" aria-label="Dotted world map"></div>
<span class="abs flink" style="left:115px;top:1116px">Home</span>
<span class="abs flink" style="left:165px;top:1116px">How it works</span>
<span class="abs flink" style="left:245px;top:1116px">Project Review</span>
<span class="abs flink" style="left:330px;top:1116px">Visit Office</span>
<span class="abs flink" style="left:113px;top:1151px">Terms of Service&nbsp; | &nbsp;Privacy Policy</span>

<div class="abs video">
  <svg class="abs" style="left:107px;top:79px" width="12" height="12" viewBox="0 0 12 12"><circle cx="6" cy="6" r="4" fill="none" stroke="#777" stroke-width="2" stroke-dasharray="2 1.5"/></svg>
  <div class="controls">
    <svg width="227" height="16"><rect x="4" y="4" width="2" height="7" fill="#333"/><rect x="8" y="4" width="2" height="7" fill="#333"/><rect x="20" y="4" width="2" height="7" fill="#333"/><path d="M28 4v7l-5-3.5z" fill="#333"/><circle cx="35" cy="8" r="3" fill="#555"/><rect x="40" y="7" width="65" height="2" fill="#555"/><rect x="110" y="4" width="36" height="8" fill="#222"/><rect x="152" y="7" width="24" height="2" fill="#555"/><path d="M180 6h3l3-3v10l-3-3h-3z" fill="#333"/><rect x="200" y="4" width="9" height="7" fill="none" stroke="#333"/><rect x="213" y="4" width="9" height="7" fill="none" stroke="#333"/></svg>
  </div>
</div>
</body>
</html>
```